Harborline Energy - needs a business card

Harborline Energy is a U.S. based diesel sourcing and distribution company that supports American oil & gas fields through providing quality product and consistent services.

Target Market(s)

Oil and Gas

Contact Information for Business Card

The background of the card must be white to ensure the logo pops.

Font styles to use
Serif
Sans Serif

Colors

Designer to choose colors to be used in the design.

Requirements
Must have
• Front of Card: Tag line: Harborline Energy, Powering America's Oil & Gas fields.
• Not sure if you guys do this part but just in case...
• Dale Menschow
• Owner/CEO
• C:555.318.4076
• E:Dmenschow@harborlineenergy.example
• W:Harborlineenergy.example
• Locations: Servicing the Powder River, DJ basin and Bakken formations.
• Back of Card: " Frac fueling is what we do. We understand how important diesel fuel is to your operation, which is why our main service line is Frac fueling. We assure our supply and stand by our service"

```html
<!DOCTYPE html>
<html lang="en">
<head>
<meta charset="utf-8">
<title>Harborline Energy — Business Card</title>
<link rel="stylesheet" href="https://fonts.googleapis.com/css2?family=Roboto:wght@400;500;700;900&family=Roboto+Condensed:wght@300;400&display=swap">
<style>
  :root {
    --navy: #0b2b5e;
    --red: #b20c0e;
    --white: #ffffff;
    --backdrop: #e4e4e4;
  }
  * { box-sizing: border-box; margin: 0; padding: 0; }
  html, body {
    width: 1125px; height: 1200px; overflow: hidden;
    background: var(--backdrop);
    font-family: "Roboto", Arial, sans-serif;
  }
  .card {
    position: absolute; left: 171px; width: 826px; height: 471px;
    overflow: hidden;
    box-shadow: 0 4px 14px rgba(0,0,0,0.18);
  }
  .card--front { top: 106px; background: var(--white); }
  .card--back { top: 640px; background: var(--red); color: var(--white); }

  .front-wave { position: absolute; inset: 0; width: 100%; height: 100%; }

  .brand {
    position: absolute; left: 57px; top: 170px; width: 270px;
    display: flex; flex-direction: column; align-items: center; gap: 16px;
  }
  .brand__dot { width: 58px; height: 58px; border-radius: 50%; background: var(--red); }
  .brand__name {
    color: var(--navy); font-weight: 900; font-size: 34px; line-height: 1.05;
    text-align: center; letter-spacing: 0.5px;
  }

  .contact {
    position: absolute; right: 37px; top: 236px; text-align: right; color: var(--white);
  }
  .contact__name { font-size: 29px; font-weight: 700; line-height: 1.1; }
  .contact__title { font-size: 19px; font-weight: 500; margin-top: 2px; }
  .contact__area { font-size: 19px; font-weight: 400; line-height: 1.3; margin-top: 14px; }
  .contact__lines { margin-top: 14px; font-size: 18.5px; line-height: 25px; }
  .contact__line { display: flex; justify-content: flex-end; align-items: center; gap: 8px; }
  .contact__line svg { width: 17px; height: 17px; flex: none; }

  .back-mark {
    position: absolute; left: 0; right: 0; top: 96px;
    display: flex; flex-direction: column; align-items: center; gap: 22px;
  }
  .back-mark__dot { width: 120px; height: 120px; border-radius: 50%; background: var(--white); }
  .back-mark__name { font-weight: 900; font-size: 40px; color: var(--white); letter-spacing: 0.5px; }

  .tagline {
    position: absolute; left: 0; right: 0; top: 346px;
    display: flex; justify-content: center; align-items: center; gap: 6px;
    font-size: 21px; font-weight: 500;
  }
  .tagline::before, .tagline::after {
    content: ""; width: 70px; height: 2px; background: var(--white);
  }
  .service-text {
    position: absolute; left: 40px; right: 40px; top: 382px;
    text-align: center; font-family: "Roboto Condensed", Arial, sans-serif;
    font-weight: 300; font-size: 18px; line-height: 24px;
  }
</style>
</head>
<body>

<section class="card card--front" aria-label="Card front">
  <svg class="front-wave" viewBox="0 0 826 471" preserveAspectRatio="none" aria-hidden="true">
    <path fill="var(--navy)" d="M0,355 C130,420 250,440 360,345 C480,230 580,80 826,88 L826,471 L0,471 Z"/>
    <path fill="none" stroke="var(--white)" stroke-width="5" d="M0,335 C130,395 255,415 355,330 C470,225 575,95 826,102"/>
    <path fill="var(--white)" d="M0,320 C140,390 260,405 350,325 C470,220 575,80 826,85 L826,0 L0,0 Z"/>
  </svg>

  <div class="brand">
    <div class="brand__dot"></div>
    <div class="brand__name">HARBORLINE ENERGY</div>
  </div>

  <div class="contact">
    <div class="contact__name">Dale Menschow</div>
    <div class="contact__title">Owner/CEO</div>
    <div class="contact__area">Servicing the Powder River<br>DJ basin &amp; Bakken formations</div>
    <div class="contact__lines">
      <div class="contact__line">555.318.4076
        <svg viewBox="0 0 16 16"><rect x="3.5" y="0.8" width="9" height="14.4" rx="1.6" fill="none" stroke="#fff" stroke-width="1.6"/><circle cx="8" cy="12.6" r="0.9" fill="#fff"/></svg>
      </div>
      <div class="contact__line">Dmenschow@harborlineenergy.example
        <svg viewBox="0 0 16 16"><rect x="0.5" y="3" width="15" height="10" fill="#fff"/><path d="M0.5,3 L8,9 L15.5,3" fill="none" stroke="var(--navy)" stroke-width="1.2"/></svg>
      </div>
      <div class="contact__line">www.Harborlineenergy.example
        <svg viewBox="0 0 16 16"><circle cx="8" cy="8" r="7.5" fill="#fff"/><path d="M4,4 C6,5 7,7 5,9 C4,11 6,12 7,14 M10,2 C9,4 11,5 12,7 C13,9 11,10 12,12" fill="none" stroke="var(--navy)" stroke-width="1.3"/></svg>
      </div>
    </div>
  </div>
</section>

<section class="card card--back" aria-label="Card back">
  <div class="back-mark">
    <div class="back-mark__dot"></div>
    <div class="back-mark__name">HARBORLINE ENERGY</div>
  </div>
  <p class="tagline">Harborline Energy, Powering America’s Oil &amp; Gas fields.</p>
  <p class="service-text">Frac fueling is what we do. We understand how important diesel fuel is to your operation, which is why our main service line is Frac fueling. We assure our supply and stand by our service</p>
</section>

</body>
</html>
```